Letterhead for New Orthopaedic Surgery Practice

My husband and I are starting our own practice named RB Spine & Vitality Center. We would like to create a nice simple but high class letterhead that doesn't use too much solid color ink when printing. I like the colors dark blue, gold, yellow. Open to other suggestions. We will need to list him and I both on the top of the letterhead. Here is the important information:
Lucinda Pryce, M.D. - Hand and Upper Extremity Surgery
Esi Dankwa, M.D. - Hip & Knee Replacement/General Orthopaedic Surgery
Location: 18735 North Bellhaven Rd
Coral Springs, FL 33071
Phone: 954-218-4635
Fax: 954-581-2264
Email: info@myrbspine.example

The only thing is that the phone and fax numbers will change once we get into our space. I just want to get the design started. I am including several documents which are my previous practice letterhead, my current procedure room letterhead, and our new Logo. The other letterheads are just for examples but please think outside of the box! We would love to see some great designs.

Colors
0054AA
0677BA
7BADD7
CADEEF
E8F1F8
0094D4
00A9DD
6FCCEA
C7EBF8
E9F6FB

Requirements
Must have
• class, elegance, luxury

```html
<!DOCTYPE html>
<html lang="en">
<head>
<meta charset="utf-8">
<title>RB Spine &amp; Vitality Center – Letterhead</title>
<link rel="stylesheet" href="https://fonts.googleapis.com/css2?family=Open+Sans:wght@600;700&display=swap">
<style>
  :root {
    --navy: #1b2a4e;
    --gold: #c4a05c;
    --white: #ffffff;
    --paper: #fdfdfd;
    --faint: #efefef;
  }
  html, body { margin: 0; padding: 0; overflow: hidden; background: var(--paper); }
  .letterhead {
    position: relative;
    width: 849px; height: 1200px;
    background: var(--paper);
    font-family: "Open Sans", Verdana, sans-serif;
    overflow: hidden;
  }
  .header-art { position: absolute; left: 0; top: 0; }
  .doctor-name, .doctor-specialty {
    position: absolute; right: 512px; margin: 0; white-space: nowrap;
  }
  .doctor-name { color: var(--white); font-weight: 700; font-size: 15px; line-height: 27px; }
  .doctor-specialty { color: var(--navy); font-weight: 700; font-size: 10.3px; line-height: 27px; }
  .name-one { top: 20px; }
  .spec-one { top: 48px; }
  .name-two { top: 75px; }
  .spec-two { top: 102px; }
  .practice-mark {
    position: absolute; left: 379px; top: 36px; width: 90px; height: 90px;
    display: flex; align-items: center; justify-content: center; text-align: center;
    color: var(--white); font-weight: 700; font-size: 9.5px; line-height: 1.25;
  }
  .contact-list { position: absolute; left: 533px; top: 20px; margin: 0; padding: 0; list-style: none; }
  .contact-item {
    height: 27.3px; line-height: 27px; font-weight: 700; font-size: 10.6px;
    color: var(--white); white-space: nowrap; letter-spacing: 0.2px;
  }
  .contact-item.on-gold { color: var(--navy); }
  .watermark {
    position: absolute; left: 415px; top: 738px; width: 420px; height: 420px;
    display: flex; align-items: center; justify-content: center; text-align: center;
    color: var(--faint); font-weight: 700; font-size: 40px; line-height: 1.2;
  }
  .watermark-ring {
    position: absolute; inset: 0; border: 3px solid var(--faint); border-radius: 50%;
  }
</style>
</head>
<body>
<div class="letterhead">
  <svg class="header-art" width="849" height="140" viewBox="0 0 849 140" aria-hidden="true">
    <rect x="0" y="47" width="849" height="28" fill="var(--gold)"/>
    <rect x="0" y="102" width="849" height="27" fill="var(--gold)"/>
    <rect x="0" y="20" width="358" height="27" fill="var(--navy)"/>
    <rect x="0" y="75" width="358" height="27" fill="var(--navy)"/>
    <rect x="490" y="20" width="359" height="27" fill="var(--navy)"/>
    <rect x="490" y="75" width="359" height="27" fill="var(--navy)"/>
    <rect x="359" y="0" width="130" height="80" fill="var(--white)"/>
    <circle cx="424" cy="80" r="65" fill="var(--white)"/>
    <rect x="369" y="0" width="110" height="80" fill="var(--gold)"/>
    <circle cx="424" cy="80" r="55" fill="var(--gold)"/>
    <circle cx="424" cy="80" r="49" fill="var(--navy)"/>
    <!-- contact icons -->
    <rect x="512" y="25" width="17" height="17" rx="3" fill="var(--white)"/>
    <path d="M520.5 28.5a4 4 0 0 1 4 4c0 3-4 6.5-4 6.5s-4-3.5-4-6.5a4 4 0 0 1 4-4z" fill="var(--navy)"/>
    <circle cx="520.5" cy="32.5" r="1.5" fill="var(--white)"/>
    <rect x="512" y="52" width="17" height="17" rx="3" fill="var(--navy)"/>
    <path d="M516 66l2-2 2 1c2-1 3-3 4-5l-1-2 2-2c1 1 1 3 0 5-1 3-4 5-6 6-1 0-2 0-3-1z" fill="var(--gold)"/>
    <rect x="512" y="80" width="17" height="17" rx="3" fill="var(--white)"/>
    <rect x="516" y="83" width="9" height="4" fill="var(--navy)"/>
    <rect x="515" y="87.5" width="11" height="6" rx="1" fill="var(--navy)"/>
    <rect x="517" y="90" width="7" height="5" fill="var(--white)" stroke="var(--navy)" stroke-width="0.8"/>
    <rect x="512" y="107" width="17" height="17" rx="3" fill="var(--navy)"/>
    <rect x="515" y="111" width="11" height="8.5" fill="none" stroke="var(--gold)" stroke-width="1"/>
    <path d="M515 111l5.5 5 5.5-5" fill="none" stroke="var(--gold)" stroke-width="1"/>
  </svg>

  <p class="doctor-name name-one">Lucinda Pryce, M.D.</p>
  <p class="doctor-specialty spec-one">Hand and Upper Extremity Surgery</p>
  <p class="doctor-name name-two">Esi Dankwa, M.D.</p>
  <p class="doctor-specialty spec-two">Hip &amp; Knee Replacement/General Orthopaedic Surgery</p>

  <div class="practice-mark">RB Spine &amp;<br>Vitality<br>Center</div>

  <ul class="contact-list">
    <li class="contact-item">18735 North Bellhaven Rd&nbsp; Coral Springs, FL 33071</li>
    <li class="contact-item on-gold">954-218-4635</li>
    <li class="contact-item">954-581-2264</li>
    <li class="contact-item on-gold">info@myrbspine.example</li>
  </ul>

  <div class="watermark">
    <div class="watermark-ring"></div>
    <span>RB Spine &amp;<br>Vitality Center</span>
  </div>
</div>
</body>
</html>
```